Brennock Holdings LLC, new Business cards

I'm moving offices and need new cards. Plus I'm open to modifying the current design of my card. I will keep the logo but would like to explore other layouts and fonts for the design. I've included the current double sided card for reference. I Like the navy color and white. Might be open to grays or silver. Needs to be clean and elegant.

Target Market(s)

Investors, buyers & sellers of private equities and real estate.

Contact Information for Business Card

Brennock Holdings
Desmond K.R. Whitfield, Managing Principal
418 Harwick Ave., Suite 310
Denver, CO 80299
M: 970-555-0147, O: 303-555-0193
Desmond@brennockholdings.example
Brennockholdings.example

Colors
0354a2
ffffff
c4c4c4

Requirements
Must have
• Business card details.
• Logo raised or embossed, it was designed after a wax seal. Current has raised ink.
Nice to have
• Space on card to write additional notes.

```html
<!DOCTYPE html>
<html lang="en">
<head>
<meta charset="utf-8">
<title>Brennock Holdings – Business Cards</title>
<link href="https://fonts.googleapis.com/css2?family=Arimo:wght@400;700&display=swap" rel="stylesheet">
<style>
  :root {
    --navy: #2b2749;
    --ink: #1e1c2e;
    --paper: #ffffff;
    --rule: #6a6880;
    --stage: #2b2b2f;
  }
  * { box-sizing: border-box; margin: 0; padding: 0; }
  html, body { width: 1200px; height: 800px; overflow: hidden; }
  body {
    background: var(--stage);
    font-family: "Arimo", Arial, sans-serif;
    display: flex;
    align-items: center;
    justify-content: center;
    gap: 40px;
  }
  .card {
    width: 525px;
    height: 300px;
    background: var(--paper);
    position: relative;
    box-shadow: 0 10px 30px rgba(0,0,0,.45);
  }
  .brand {
    position: absolute;
    left: 36px;
    top: 50%;
    transform: translateY(-50%);
    display: flex;
    align-items: center;
    gap: 12px;
  }
  .brand-dot {
    width: 34px;
    height: 34px;
    border-radius: 50%;
    background: var(--navy);
    flex: none;
  }
  .brand-name {
    color: var(--navy);
    font-weight: 700;
    font-size: 19px;
    letter-spacing: .04em;
    text-transform: uppercase;
    line-height: 1.15;
    width: 130px;
  }
  /* Note side */
  .notes {
    position: absolute;
    left: 250px;
    right: 32px;
    top: 40px;
  }
  .notes-label {
    color: var(--navy);
    font-weight: 700;
    font-size: 15px;
    margin-bottom: 10px;
  }
  .notes-line {
    border-bottom: 1.5px dotted var(--rule);
    height: 27px;
  }
  /* Contact side */
  .contact {
    position: absolute;
    left: 250px;
    right: 24px;
    top: 58px;
    color: var(--ink);
  }
  .contact-name {
    font-weight: 700;
    font-size: 18px;
    color: var(--navy);
    text-transform: uppercase;
    letter-spacing: .01em;
  }
  .contact-title { font-size: 13px; margin-top: 3px; }
  .contact-address { font-size: 13px; margin-top: 18px; line-height: 1.4; }
  .contact-lines { font-size: 13px; margin-top: 8px; line-height: 1.5; }
  .contact-lines b { font-weight: 700; }
  .contact-web { font-size: 13px; margin-top: 10px; }
</style>
</head>
<body>
  <section class="card card--notes">
    <div class="brand">
      <span class="brand-dot"></span>
      <span class="brand-name">Brennock Holdings</span>
    </div>
    <div class="notes">
      <p class="notes-label">Note</p>
      <div class="notes-line"></div>
      <div class="notes-line"></div>
      <div class="notes-line"></div>
      <div class="notes-line"></div>
      <div class="notes-line"></div>
      <div class="notes-line"></div>
      <div class="notes-line"></div>
    </div>
  </section>

  <section class="card card--contact">
    <div class="brand">
      <span class="brand-dot"></span>
      <span class="brand-name">Brennock Holdings</span>
    </div>
    <div class="contact">
      <p class="contact-name">Desmond K.R. Whitfield</p>
      <p class="contact-title">Managing Principal</p>
      <p class="contact-address">418 Harwick Ave., Suite 310<br>Denver, CO 80299</p>
      <p class="contact-lines"><b>M:</b> 970-555-0147 | <b>O:</b> 303-555-0193<br><b>E:</b> Desmond@brennockholdings.example</p>
      <p class="contact-web">Brennockholdings.example</p>
    </div>
  </section>
</body>
</html>
```